RLG Biz Cards and Web Page Design

Hello we are a credit card processing company, a lending company, and payroll company. Seeing how this is a card. I would like to see some clever designs... You could make it look like a credit card, with raised lettering and signature spot on the back. Be creative.
Also this is for a webpage. Our website is www.ridgecrestledgergroup.com
Please let me know what you need.

Target Market(s)

Business Owners in the USA.

Industry/Entity Type

Credit Card

Contact Information for Business Card

I've attached our current logo and business cards. I would like you to use the Red, White, and Blue Colors and also maybe try designs that look like credit cards with Raised Text, signature spot in the back and mag strips.

Number of Pages Required

1 page

```html
<!DOCTYPE html>
<html lang="en">
<head>
<meta charset="utf-8">
<title>Ridgecrest Ledger Group – Business Card</title>
<link href="https://fonts.googleapis.com/css2?family=Montserrat:wght@600;700&family=Arimo:ital,wght@0,400;0,700;1,400&display=swap" rel="stylesheet">
<style>
  :root {
    --red: #e01b24;
    --red-deep: #b0121c;
    --navy: #1a2070;
    --navy-deep: #0f1450;
    --blue-mid: #2a3590;
    --silver: #d4d4d6;
    --white: #ffffff;
    --paper: #f5f5f7;
    --ink: #111111;
    --gold: #d8c27a;
  }
  * { box-sizing: border-box; margin: 0; padding: 0; }
  html, body { width: 1200px; height: 1200px; overflow: hidden; background: var(--white); }
  body { position: relative; font-family: "Arimo", Arial, sans-serif; }

  .card {
    position: absolute;
    border-radius: 22px;
    overflow: hidden;
    box-shadow: 0 10px 30px rgba(0,0,0,0.12);
  }

  /* ---------- Back side ---------- */
  .card-back { left: 210px; top: 110px; width: 780px; height: 330px; background: var(--navy); }
  .back-top {
    height: 150px;
    background: linear-gradient(90deg, var(--red-deep), var(--red));
    display: flex; align-items: center; justify-content: center;
  }
  .stripes {
    height: 40px;
    background: repeating-linear-gradient(180deg, var(--white) 0 5px, #e3e4f2 5px 9px);
  }
  .services {
    height: 80px;
    background: linear-gradient(90deg, var(--blue-mid), var(--navy-deep));
    display: flex; align-items: center;
  }
  .service {
    flex: 1; text-align: center; color: var(--white);
    font-weight: 700; font-size: 15px; line-height: 1.25;
  }
  .service + .service { border-left: 2px solid var(--white); }
  .web-band {
    height: 32px; background: var(--silver);
    display: flex; align-items: center; justify-content: center;
    font-size: 15px; letter-spacing: 4px; color: var(--ink);
  }
  .back-bottom { height: 28px; background: linear-gradient(90deg, var(--blue-mid), var(--navy)); }

  /* ---------- Logo lockup ---------- */
  .brand { display: flex; align-items: center; gap: 16px; font-family: "Montserrat", sans-serif; font-weight: 700; }
  .brand-mark { width: 34px; height: 34px; border: 4px solid currentColor; border-radius: 4px; }
  .brand-initials { font-size: 44px; letter-spacing: 1px; }
  .brand-rule { width: 2px; align-self: stretch; background: currentColor; }
  .brand-name { font-size: 19px; letter-spacing: 2px; line-height: 1.2; }
  .brand-light { color: var(--white); height: 100px; }
  .brand-dark { color: var(--navy); height: 90px; }

  /* ---------- Front side ---------- */
  .card-front { left: 205px; top: 620px; width: 790px; height: 362px; background: var(--navy); }
  .front-shape { position: absolute; inset: 0; }
  .front-content { position: absolute; inset: 0; }
  .front-content .brand { position: absolute; left: 45px; top: 40px; }
  .chip {
    position: absolute; left: 45px; top: 150px; width: 100px; height: 58px;
    border-radius: 10px; background: linear-gradient(135deg, #efe2a8, var(--gold) 60%, #a8904a);
    border: 2px solid #5a4a20;
  }
  .person-name { position: absolute; left: 43px; top: 228px; font-family: "Montserrat", sans-serif; font-weight: 700; font-size: 27px; color: var(--navy); }
  .person-title { position: absolute; left: 43px; top: 264px; font-style: italic; font-size: 20px; color: var(--red); }
  .person-cell { position: absolute; left: 42px; top: 294px; font-size: 28px; color: var(--navy); }

  .map {
    position: absolute; left: 580px; top: 45px; width: 150px; height: 80px;
    border-radius: 14px 30px 20px 26px;
    background: linear-gradient(135deg, #f2f2f4, #b9bac4);
  }
  .contact {
    position: absolute; right: 38px; top: 188px; text-align: right;
    color: var(--white); font-size: 17px; line-height: 1.25;
  }
  .phones {
    position: absolute; right: 36px; top: 292px; text-align: right;
    color: var(--white); font-size: 17px; line-height: 1.3;
  }
  .phones b { font-weight: 700; }
</style>
</head>
<body>

  <section class="card card-back" aria-label="Business card back">
    <div class="back-top">
      <div class="brand brand-light">
        <span class="brand-mark"></span>
        <span class="brand-initials">RLG</span>
        <span class="brand-rule"></span>
        <span class="brand-name">RIDGECREST<br>LEDGER GROUP</span>
      </div>
    </div>
    <div class="stripes"></div>
    <div class="services">
      <div class="service">MERCHANT<br>CASH ADVANCE</div>
      <div class="service">CREDIT CARD<br>PROCESSING</div>
      <div class="service">PAYROLL &amp;<br>HUMAN RESOURCES</div>
    </div>
    <div class="web-band">www.ridgecrestledgergroup.com</div>
    <div class="back-bottom"></div>
  </section>

  <section class="card card-front" aria-label="Business card front">
    <svg class="front-shape" width="790" height="362" viewBox="0 0 790 362" aria-hidden="true">
      <defs>
        <linearGradient id="navyFade" x1="0" y1="0" x2="1" y2="1">
          <stop offset="0" stop-color="#2a3590"/>
          <stop offset="1" stop-color="#0f1450"/>
        </linearGradient>
      </defs>
      <rect width="790" height="362" fill="url(#navyFade)"/>
      <path d="M0 0 H398 C490 60 505 260 360 362 H0 Z" fill="#c4141e"/>
      <path d="M0 0 H375 C458 60 470 250 330 362 H0 Z" fill="#f5f5f7"/>
    </svg>

    <div class="front-content">
      <div class="brand brand-dark">
        <span class="brand-mark"></span>
        <span class="brand-initials">RLG</span>
        <span class="brand-rule"></span>
        <span class="brand-name">RIDGECREST<br>LEDGER GROUP</span>
      </div>

      <div class="chip" role="img" aria-label="Payment card chip"></div>

      <div class="person-name">Daniel R. Whitford</div>
      <div class="person-title">Director of Operations</div>
      <div class="person-cell">(C) 860-555-0147</div>

      <div class="map" role="img" aria-label="Silver map of the United States"></div>

      <div class="contact">
        418 Harbor Lane<br>
        Milford, CT 06460<br>
        d.whitford@ridgecrestledger.com
      </div>
      <div class="phones">
        <b>(O)</b> 888-555-0192<br>
        <b>(F)</b> 877-555-0168
      </div>
    </div>
  </section>

</body>
</html>
```